Photography Prints Business Card Design

Background info: Nature, flower, landscape,  macro, wildlife photographer. Shoot color and B&W images. Sell prints at juried fine art shows.
Looking for two-sided, clean, memorable design with creative use of my initials, DH.   I like the DH symbol in the my logo. Just use the DH symbol. Do not leave the underlying text as uploaded by me. I do not like the serif font and positioning of the words!  Either  remove the small print "Dorian Hallet Photography" under the logo,  or change to a sans serif font, or reposition with "Dorian Hallet" above "Photography" which seems to work with serif fonts.
Target Market(s)
Sophisticated art buyers, post-college to middle age
Industry/Entity Type
Business
Contact Information for Business Card
Dorian Hallet Photography
728 Maple Brook CT
Winston-Salem, NC 27127
(336) 555-0148
www.dorianhallet.com
CP:halletphoto
dorian@dorianhallet.com
If using just one line address, make sure there is a comma after  "CT" in street address. For example:
728 Maple Brook CT, Winston-Salem, NC 27127
Requirements
Must have
- 1.Two-sided card submitted as one design.
2. Must use the DH symbol in my logo.
3. Do not leave the text "Dorian Hallet Photography" under the DH symbol in the logo uploaded by me. I do not like that serif font or the positioning of the words! Either remove the small print "Dorian Hallet Photography" under the logo entirely, or change text to a sans serif font, or reposition text with "Dorian Hallet" above "Photography" which seems to work with serif fonts.
Nice to have
- Can use my DH logo (three file types uploaded: AI, PSD, TIF)  I  like the attached B&W water droplet photo.  My pictures on my website, www.dorianhhallet.com  can also be used.  Possible use of Chirply logo with (either the "f" alone or the square blue icon with white "f") my CP page short url name: halletphoto.
Should not have
- 1.No icons or pictures  of camera or lenses or other photographic gear or film strips.
2. No QR or other "barcode" type symbols.
3. No outlining of my logo symbol (drop shadow possibly).
4. No decorative or outlined fonts.
5. I am not a fan of most script fonts.
6. No play on "Hallet" such as snow or other winter season symbols.
7. Do not keep the original text, "Dorian Hallet Photography" under DH logo. Change it or remove it entirely.

```html
<!DOCTYPE html>
<html lang="en">
<head>
<meta charset="utf-8">
<title>Dorian Hallet Photography – Business Card</title>
<link rel="stylesheet" href="https://fonts.googleapis.com/css2?family=Cinzel:wght@400&family=Libre+Baskerville&family=Montserrat:ital,wght@0,500;1,700&display=swap">
<style>
  :root {
    --canvas: #d9d9d9;
    --card-white: #ffffff;
    --ink: #111111;
    --ink-soft: #2a2a2a;
    --brand-blue: #3b5998;
    --water-deep: #081524;
    --water-mid: #1d3856;
    --water-light: #7f9bb8;
    --glow: #f4f6f8;
    --plumage: #eef1f4;
    --drop-dark: #050505;
    --drop-mid: #6b6b6b;
    --drop-light: #f0f0f0;
  }
  * { box-sizing: border-box; margin: 0; padding: 0; }
  html, body { width: 1200px; height: 1200px; overflow: hidden; }
  body {
    background: var(--canvas);
    display: flex; flex-direction: column; align-items: center; justify-content: center;
    gap: 40px;
  }
  .card {
    position: relative; width: 900px; height: 514px;
    background: var(--card-white); overflow: hidden;
    box-shadow: 0 6px 18px rgba(0,0,0,.18);
  }

  /* Front side */
  .front__photo {
    position: absolute; inset: 0 0 114px 0;
    background:
      radial-gradient(circle at 80% 24%, var(--glow) 0, rgba(244,246,248,.9) 13%, rgba(127,155,184,.35) 30%, transparent 46%),
      radial-gradient(ellipse 230px 110px at 36% 26%, var(--plumage) 0, rgba(238,241,244,.7) 40%, transparent 100%),
      radial-gradient(ellipse 500px 90px at 40% 78%, rgba(127,155,184,.45) 0, transparent 100%),
      linear-gradient(180deg, var(--water-deep) 0%, var(--water-mid) 58%, var(--water-deep) 100%);
  }
  .front__logo {
    position: absolute; top: 34px; right: 96px; width: 220px; text-align: center;
    font-family: "Montserrat", sans-serif; font-weight: 500; color: var(--ink);
  }
  .front__monogram { font-size: 96px; line-height: 1; letter-spacing: -2px; }
  .front__wordmark { margin-top: 10px; font-size: 14px; letter-spacing: 3px; line-height: 1.4; }
  .front__band {
    position: absolute; left: 0; right: 0; bottom: 0; height: 114px;
    display: flex; align-items: center; padding: 0 50px;
    font-family: "Montserrat", sans-serif; font-style: italic; font-weight: 700;
    font-size: 24px; color: var(--ink);
  }
  .front__web { display: flex; align-items: center; gap: 18px; }
  .front__globe { width: 30px; height: 30px; }
  .front__divider { width: 2px; height: 48px; background: var(--ink); margin: 0 38px; }
  .front__social { display: flex; align-items: center; gap: 16px; }
  .front__network { color: var(--brand-blue); }

  /* Back side */
  .back__photo {
    position: absolute; inset: 0;
    background:
      radial-gradient(ellipse 90px 70px at 13% 36%, rgba(230,230,230,.55) 0, transparent 100%),
      radial-gradient(ellipse 70px 55px at 57% 33%, rgba(230,230,230,.5) 0, transparent 100%),
      radial-gradient(ellipse 50px 40px at 86% 34%, rgba(230,230,230,.45) 0, transparent 100%),
      linear-gradient(180deg, var(--drop-dark) 0%, #141414 24%, var(--drop-mid) 46%, #cdcdcd 66%, var(--drop-light) 100%);
  }
  .back__title {
    position: absolute; top: 44px; left: 0; right: 0; text-align: center;
    font-family: "Cinzel", serif; font-weight: 400; font-size: 30px; letter-spacing: 2px; color: #ffffff;
  }
  .back__name {
    position: absolute; left: 56px; bottom: 112px; width: 290px;
    font-family: "Libre Baskerville", serif; font-size: 25px; white-space: nowrap; color: var(--ink);
  }
  .back__divider {
    position: absolute; left: 370px; bottom: 54px; width: 2px; height: 170px; background: var(--ink);
  }
  .back__contact {
    position: absolute; left: 400px; bottom: 72px;
    font-family: "Libre Baskerville", serif; font-size: 18px; line-height: 2.1; color: var(--ink-soft);
    list-style: none; white-space: nowrap;
  }
</style>
</head>
<body>
  <section class="card card--front">
    <div class="front__photo" role="img" aria-label="Photograph of a white egret taking off from dark blue water with splashing droplets"></div>
    <div class="front__logo">
      <div class="front__monogram">DH</div>
      <div class="front__wordmark">DORIAN<br>HALLET<br>PHOTOGRAPHY</div>
    </div>
    <div class="front__band">
      <div class="front__web">
        <svg class="front__globe" viewBox="0 0 30 30" fill="none" stroke="#3b5998" stroke-width="2">
          <circle cx="15" cy="15" r="13"/>
          <ellipse cx="15" cy="15" rx="6" ry="13"/>
          <line x1="2" y1="15" x2="28" y2="15"/>
          <line x1="4" y1="8" x2="26" y2="8"/>
          <line x1="4" y1="22" x2="26" y2="22"/>
        </svg>
        <span>WWW.DORIANHALLET.COM</span>
      </div>
      <div class="front__divider"></div>
      <div class="front__social">
        <span class="front__network">Chirply</span>
        <span>HALLETPHOTO</span>
      </div>
    </div>
  </section>

  <section class="card card--back">
    <div class="back__photo" role="img" aria-label="Black and white macro photograph of clear water droplets resting on a leaf"></div>
    <h1 class="back__title">Dorian Hallet Photography</h1>
    <p class="back__name">DORIAN HALLET</p>
    <div class="back__divider"></div>
    <ul class="back__contact">
      <li>728 Maple Brook CT, Winston-Salem, NC 27127</li>
      <li>Phone : (336) 555-0148</li>
      <li>Email : dorian@dorianhallet.com</li>
    </ul>
  </section>
</body>
</html>
```